School Learner profile graphic representation

I have a set of ideas around communicating our school 'learner profile'. These represent the attitudes, habits and dispositions we are trying to develop through our curriculum and wider enrichment programme. I want the links between the ideas and concepts to be represented in some form of an inforgraphic which can be published and displayed for the whole community to connect with. we run two schools and want the profile to represent for both.

Target Market(s)

Students, Parents, Teachers, Wider community in education

Industry/Entity Type

Education

Font styles to use
Other font styles liked:
• Johnson p22

Colors

Designer to choose colors to be used in the design.

Requirements
Must have
• See my diagram in the ppt.
• The statements Aspiration, Agency, Agility, Altitude with the supporting descriptions. Ideally the values in the center is also represented. The two school logos should also be present somehow (both emblems at least). Let me know if the full logo files are required
Nice to have
• the numbering shown in my diagram is not absolutely necessary is it is not necessarily a linear process and rather cyclical and cross reinforcing

```html
<!DOCTYPE html>
<html lang="en">
<head>
<meta charset="utf-8">
<title>Envisioning Our Learners</title>
<link rel="stylesheet" href="https://fonts.googleapis.com/css2?family=Jost:wght@400;500;700&display=swap">
<style>
  :root {
    --ink: #111111;
    --text: #222222;
    --paper: #ffffff;
    --red: #e8262b;
    --red-soft: #ee3b3f;
    --red-deep: #e01f25;
    --orange: #f7a21b;
    --blue: #3a9ad9;
    --pink: #ee4a9c;
    --teal: #1fc7b8;
  }
  * { margin: 0; padding: 0; box-sizing: border-box; }
  html, body { width: 1200px; height: 827px; overflow: hidden; background: var(--paper); }
  body { font-family: "Jost", "Century Gothic", sans-serif; color: var(--text); }
  .canvas { position: relative; width: 1200px; height: 827px; }

  .school { position: absolute; display: flex; align-items: center; gap: 14px; }
  .school-mark { width: 90px; height: 90px; border-radius: 50%; background: var(--red); flex: none; }
  .school--private { left: 57px; top: 58px; }
  .school--private .school-name { font-size: 21px; font-weight: 700; color: var(--ink); letter-spacing: -0.3px; }
  .school--community { left: 790px; top: 54px; }
  .school--community .school-name {
    font-size: 27px; font-weight: 500; color: var(--red); letter-spacing: 3px; line-height: 1.3; text-transform: uppercase;
  }

  .title {
    position: absolute; top: 198px; left: 0; width: 1200px; text-align: center;
    font-size: 42px; font-weight: 700; color: var(--ink);
  }

  .profile { position: absolute; width: 400px; }
  .profile-heading { font-size: 26px; font-weight: 400; line-height: 1.2; margin-bottom: 8px; }
  .profile-heading strong { font-weight: 700; }
  .profile-text { font-size: 23px; line-height: 1.32; color: var(--text); }
  .profile--altitude { left: 55px; top: 325px; }
  .profile--altitude .profile-heading { color: var(--orange); }
  .profile--agency { left: 797px; top: 325px; }
  .profile--agency .profile-heading { color: var(--blue); }
  .profile--agility { left: 55px; top: 677px; }
  .profile--agility .profile-heading { color: var(--teal); }
  .profile--aspiration { left: 807px; top: 677px; }
  .profile--aspiration .profile-heading { color: var(--pink); }

  .wheel { position: absolute; left: 0; top: 0; }
  .wheel-label { font-family: "Jost", "Century Gothic", sans-serif; font-size: 26px; fill: #ffffff; }
  .wheel-core { font-family: "Jost", "Century Gothic", sans-serif; font-size: 25px; fill: var(--ink); text-anchor: middle; }
</style>
</head>
<body>
<div class="canvas">

  <div class="school school--private">
    <span class="school-mark"></span>
    <span class="school-name">Cedar Grove Private School</span>
  </div>

  <div class="school school--community">
    <span class="school-mark"></span>
    <span class="school-name">Cedar Grove<br>Community<br>School</span>
  </div>

  <h1 class="title">Envisioning Our Learners</h1>

  <div class="profile profile--altitude">
    <h2 class="profile-heading">Learners with <strong>Altitude</strong></h2>
    <p class="profile-text">Achieve great things and<br>work to elevate others</p>
  </div>

  <div class="profile profile--agency">
    <h2 class="profile-heading">Learners with <strong>Agency</strong></h2>
    <p class="profile-text">Believe in their capacity and<br>responsibility to do great things</p>
  </div>

  <div class="profile profile--agility">
    <h2 class="profile-heading">Learners with <strong>Agility</strong></h2>
    <p class="profile-text">Are determined, equipped and<br>able to accomplish great things</p>
  </div>

  <div class="profile profile--aspiration">
    <h2 class="profile-heading">Learners with <strong>Aspiration</strong></h2>
    <p class="profile-text">Inspired and Believe in<br>pursuing great things</p>
  </div>

  <svg class="wheel" width="1200" height="827" viewBox="0 0 1200 827" aria-label="Learner profile wheel">
    <defs>
      <path id="arc-mind" d="M587 402 A135 135 0 0 1 703.9 604.5"/>
      <path id="arc-spirit" d="M470.1 604.5 A135 135 0 0 1 587 402"/>
      <path id="arc-heart" d="M448.4 617 A160 160 0 0 0 725.6 617"/>
    </defs>

    <g class="wheel-ring" fill="none" stroke-width="11">
      <path d="M361 537 A226 226 0 0 1 587 311" stroke="var(--orange)"/>
      <path d="M587 311 A226 226 0 0 1 813 537" stroke="var(--blue)"/>
      <path d="M813 537 A226 226 0 0 1 587 763" stroke="var(--pink)"/>
      <path d="M587 763 A226 226 0 0 1 361 537" stroke="var(--teal)"/>
    </g>

    <g class="wheel-segments" stroke="#ffffff" stroke-opacity="0.35" stroke-width="1">
      <path d="M587 339 A198 198 0 0 1 758.5 636 L671.9 586 A98 98 0 0 0 587 439 Z" fill="var(--red)"/>
      <path d="M758.5 636 A198 198 0 0 1 415.5 636 L502.1 586 A98 98 0 0 0 671.9 586 Z" fill="var(--red-soft)"/>
      <path d="M415.5 636 A198 198 0 0 1 587 339 L587 439 A98 98 0 0 0 502.1 586 Z" fill="var(--red-deep)"/>
    </g>

    <text class="wheel-label"><textPath href="#arc-mind" startOffset="50%" text-anchor="middle">Mind</textPath></text>
    <text class="wheel-label"><textPath href="#arc-spirit" startOffset="50%" text-anchor="middle">Attitude and Spirit</textPath></text>
    <text class="wheel-label"><textPath href="#arc-heart" startOffset="50%" text-anchor="middle">Heart</textPath></text>

    <g class="wheel-core">
      <text x="587" y="497">Values</text>
      <text x="587" y="532">Morals</text>
      <text x="587" y="566">Principles</text>
      <text x="587" y="600">Ethics</text>
    </g>
  </svg>

</div>
</body>
</html>
```